Brett Olsen Building Business Card Design

Hi,

I need a business card for my Building company.
I am a Builder and build homes for clients.
I am looking for a sophisticated logo that can be used on business cards, envelopes and letter heads.
I am trying to take my business to the next level and need a professional business card.

Colours: Please use white, black, dark grey and bright blue.

Thank you,

Carol and Brett.

Target Market(s)

1. Home and Building Companies 2. Potential customers

Industry/Entity Type

Business

Contact Information for Business Card

Brett Olsen Building PTY LTD

Brett Olsen

Director

A.B.N. 37 829 516 073

BUILDERS LICENCE No. 573019k

Mobile: 0412 907 381

Email: brettolsenbuilding@mailvane.com.au

Requirements
Must have
• The following is compulsory to have in the designs:

Brett Olsen Building PTY LTD (business name)

Brett Olsen (contact name)

Director (position)

A.B.N. 37 829 516 073

Builders Licence No. 573019k

Mobile: 0412 907 381

Nice to have
• Logo for business
Should not have
• Should not be cluttered.

I am looking for a clean, sophisticated and professional business card design.

```html
<!DOCTYPE html>
<html lang="en">
<head>
<meta charset="utf-8">
<title>Brett Olsen Building – Business Cards</title>
<link rel="stylesheet" href="https://fonts.googleapis.com/css2?family=Roboto+Slab:wght@400&family=Roboto+Condensed:wght@400&display=swap">
<style>
  :root {
    --stage: #000000;
    --card-grey: #7c7d80;
    --bright-blue: #0aade8;
    --white: #ffffff;
    --ink: #111111;
  }
  * { margin: 0; padding: 0; box-sizing: border-box; }
  html, body { width: 1200px; height: 823px; overflow: hidden; background: var(--stage); }
  .stage { position: relative; width: 1200px; height: 823px; }

  .card {
    position: absolute;
    width: 524px;
    height: 291px;
    background: var(--card-grey);
    overflow: hidden;
  }
  .card--front-grey { left: 54px; top: 111px; }
  .card--front-split { left: 600px; top: 111px; }
  .card--back-light { left: 54px; top: 416px; }
  .card--back-dark { left: 600px; top: 416px; }

  .card__white-panel {
    position: absolute; left: 0; top: 0; width: 229px; height: 100%;
    background: var(--white);
  }

  /* brand lockup: plain square + business name */
  .brand {
    position: absolute;
    display: flex; flex-direction: column; align-items: center;
    font-family: "Roboto Slab", serif;
    font-weight: 400;
    text-align: center;
  }
  .brand__square { width: 54px; height: 54px; background: var(--bright-blue); margin-bottom: 16px; }
  .brand__name { font-size: 22px; line-height: 1.1; }
  .brand--light .brand__name { color: var(--white); }
  .brand--dark .brand__name { color: var(--ink); }
  .card--front-grey .brand, .card--front-split .brand { left: 14px; top: 62px; width: 200px; }
  .card--back-light .brand, .card--back-dark .brand { left: 162px; top: 78px; width: 200px; }

  .details { position: absolute; left: 263px; top: 0; right: 0; height: 100%; color: var(--white); }
  .details__name { position: absolute; top: 48px; left: 0; font-family: "Roboto Slab", serif; font-size: 21px; }
  .details__role { position: absolute; top: 78px; left: 0; font-family: "Roboto Slab", serif; font-size: 16px; }
  .details__rule { position: absolute; left: 0; right: 0; height: 3px; background: var(--bright-blue); }
  .details__rule--top { top: 110px; }
  .details__rule--bottom { top: 185px; }
  .details__registration { position: absolute; top: 129px; left: 0; font-family: "Roboto Slab", serif; font-size: 12.5px; line-height: 21px; }
  .details__contact { position: absolute; top: 208px; left: 0; font-family: "Roboto Condensed", sans-serif; font-size: 16px; line-height: 31px; }
  .details__label { color: var(--bright-blue); }
</style>
</head>
<body>
<main class="stage">

  <section class="card card--front-grey">
    <div class="brand brand--light">
      <span class="brand__square"></span>
      <span class="brand__name">Brett Olsen<br>Building PTY LTD</span>
    </div>
    <div class="details">
      <p class="details__name">Brett Olsen</p>
      <p class="details__role">Director</p>
      <span class="details__rule details__rule--top"></span>
      <p class="details__registration">A.B.N. 37 829 516 073<br>BUILDERS LICENCE No. 573019k</p>
      <span class="details__rule details__rule--bottom"></span>
      <p class="details__contact"><span class="details__label">M:</span> 0412 907 381<br><span class="details__label">E:</span> brettolsenbuilding@mailvane.com.au</p>
    </div>
  </section>

  <section class="card card--front-split">
    <div class="card__white-panel"></div>
    <div class="brand brand--dark">
      <span class="brand__square"></span>
      <span class="brand__name">Brett Olsen<br>Building PTY LTD</span>
    </div>
    <div class="details">
      <p class="details__name">Brett Olsen</p>
      <p class="details__role">Director</p>
      <span class="details__rule details__rule--top"></span>
      <p class="details__registration">A.B.N. 37 829 516 073<br>BUILDERS LICENCE No. 573019k</p>
      <span class="details__rule details__rule--bottom"></span>
      <p class="details__contact"><span class="details__label">M:</span> 0412 907 381<br><span class="details__label">E:</span> brettolsenbuilding@mailvane.com.au</p>
    </div>
  </section>

  <section class="card card--back-light">
    <div class="brand brand--light">
      <span class="brand__square"></span>
      <span class="brand__name">Brett Olsen<br>Building PTY LTD</span>
    </div>
  </section>

  <section class="card card--back-dark">
    <div class="brand brand--dark">
      <span class="brand__square"></span>
      <span class="brand__name">Brett Olsen<br>Building PTY LTD</span>
    </div>
  </section>

</main>
</body>
</html>
```